Join us at the 19th Rhythm of Tallowbrook Music Festival for two nights of music, art and food. July 11, 2014 from 5:00 pm to 12 midnight "Every Little Beat" featuring the vocals of Ms. Lorita Vance. On July 12, 2014 "Tallowbrook Swing" featuring Calvin "Firefly" Rudley and the 19th annual Tallowbrook Parade. Come sample the local food vendors, view neighborhood art and crafts. Come and experience the amazing Junior Ensemble Institute - Road Stage . For further information call Marlene Copley at 216 555-0137 or visit our web site at www.tallowbrookunion.org. the Tallowbrook Marlow Cedar Ridge neighborhoods are MXL accessible and just 5 miles from east of Downtown Harlan Falls. The Rhythm of Tallowbrook is an annual music festival featuring local talents come join us for two nights of entertainment and good food.

```html
<!DOCTYPE html>
<html lang="en">
<head>
<meta charset="utf-8">
<title>19th Rhythm of Tallowbrook Music Festival</title>
<link rel="stylesheet" href="https://fonts.googleapis.com/css2?family=Arimo:ital,wght@0,400;0,700;1,400;1,700&family=Archivo+Narrow:wght@400&family=Kaushan+Script&display=swap">
<style>
  :root {
    --ink: #111111;
    --paper: #ffffff;
    --badge: #7d7d7d;
    --frame: #c6c6c6;
    --head-top: #000000;
    --head-bottom: #ffffff;
    --title-soft: #e4e4e4;
  }
  html, body { margin: 0; padding: 0; overflow: hidden; background: var(--paper); }
  .flyer {
    position: relative; width: 1200px; height: 926px; box-sizing: border-box;
    border: 2px solid var(--ink); background: var(--paper); color: var(--ink);
    font-family: "Arimo", Arial, sans-serif; overflow: hidden;
  }
  .abs { position: absolute; }
  .center { text-align: center; }
  .masthead {
    left: 34px; top: 36px; width: 524px; height: 180px;
    background: linear-gradient(to bottom, var(--head-top) 0%, #3a3a3a 35%, #9a9a9a 70%, var(--head-bottom) 100%);
  }
  .invite {
    left: 34px; top: 42px; width: 524px; font-family: "Kaushan Script", cursive;
    font-size: 32px; color: var(--paper); line-height: 1;
  }
  .title-line {
    left: 34px; width: 524px; font-weight: 700; color: var(--paper); line-height: 1; white-space: nowrap;
  }
  .title-main { top: 94px; font-size: 30px; }
  .title-main small { font-size: 20px; }
  .title-sub { top: 139px; font-size: 45px; color: var(--title-soft); }
  .venue { left: 34px; top: 194px; width: 524px; font-size: 20px; }
  .free {
    left: 40px; top: 226px; font-weight: 700; font-style: italic; font-size: 34px;
    transform: rotate(-13deg); transform-origin: left bottom; letter-spacing: 1px;
  }
  .featuring { left: 178px; top: 224px; font-weight: 700; font-size: 24px; }
  .perk { font-size: 20px; white-space: nowrap; }
  .schedule {
    left: 38px; top: 326px; width: 522px; height: 184px; box-sizing: border-box;
    border: 4px solid var(--frame);
  }
  .schedule-head { left: 0; top: 12px; width: 514px; font-weight: 700; font-size: 22px; letter-spacing: 1.3px; }
  .date-badge {
    background: var(--badge); color: var(--paper); font-weight: 700; font-size: 20px;
    padding: 1px 8px; letter-spacing: .5px;
  }
  .slot { font-size: 20px; white-space: nowrap; }
  .show { font-style: italic; font-size: 20px; white-space: nowrap; }
  .show small { font-size: 16px; }
  .invite-line { left: 34px; width: 524px; font-weight: 700; font-style: italic; font-size: 23px; top: 521px; }
  .ensemble { left: 34px; width: 524px; font-size: 22px; top: 556px; white-space: nowrap; }
  .info { left: 34px; width: 524px; font-size: 20px; }
  .web-band {
    left: 36px; top: 657px; width: 510px; height: 35px; background: var(--ink); color: var(--paper);
    font-weight: 700; font-style: italic; font-size: 27px; line-height: 35px; letter-spacing: .5px;
  }
  .transit-note {
    left: 35px; top: 706px; width: 106px; height: 180px; box-sizing: border-box;
    border: 1.5px solid var(--ink); font-family: "Archivo Narrow", "Arial Narrow", sans-serif;
    font-size: 14px; line-height: 18.5px; padding-top: 5px; white-space: nowrap;
  }
</style>
</head>
<body>
<main class="flyer">
  <div class="abs masthead"></div>
  <div class="abs invite center">Join us for the</div>
  <h1 class="abs title-line title-main center" style="margin:0">19<small>TH</small> RHYTHM <small>OF</small> TALLOWBROOK</h1>
  <div class="abs title-line title-sub center">MUSIC FESTIVAL</div>
  <div class="abs venue center">Mini Park &nbsp;•&nbsp; E. 142 Tallowbrook</div>

  <div class="abs free">FREE!</div>
  <div class="abs featuring">FEATURING</div>
  <div class="abs perk" style="left:104px;top:259px">• LOCAL TALENTS</div>
  <div class="abs perk" style="left:304px;top:259px">• LOCAL FOOD VENDORS</div>
  <div class="abs perk" style="left:104px;top:290px">• NEIGHBORHOOD ART AND CRAFTS</div>

  <section class="abs schedule">
    <div class="abs schedule-head center">2 NIGHTS OF MUSIC, ART AND FOOD</div>
    <span class="abs date-badge" style="left:79px;top:41px">JULY 11, 2014</span>
    <span class="abs slot" style="left:270px;top:44px;font-size:17px">5 pm - 12 midnight</span>
    <div class="abs show" style="left:18px;top:70px">"Every Little Beat" <small>featuring the vocals of Ms. Lorita Vance</small></div>
    <span class="abs date-badge" style="left:14px;top:110px">JULY 12, 2014</span>
    <span class="abs slot" style="left:192px;top:112px">19th Annual Tallowbrook Parade</span>
    <div class="abs show" style="left:12px;top:140px">and "Tallowbrook Swing" <small>featuring Calvin "Firefly" Rudley</small></div>
  </section>

  <div class="abs invite-line center">Come and experience the amazing</div>
  <div class="abs ensemble center">JUNIOR ENSEMBLE INSTITUTE - ROAD STAGE</div>
  <div class="abs info center" style="top:596px">For further information</div>
  <div class="abs info center" style="top:627px">Call Marlene Copley at 216 555-0137 or visit</div>
  <div class="abs web-band center">WWW.TALLOWBROOKUNION.ORG</div>

  <aside class="abs transit-note center">The Tallowbrook<br>Marlow<br>Cedar Ridge<br>neighborhoods<br>are MXL accessible<br>and just 5 miles<br>from east of<br>Downtown<br>Harlan Falls.</aside>
</main>
</body>
</html>
```